Technical Communications firm needs an article turned into a white paper

We want to redesign a 3-part blog series into a white paper that we can print for a conference. I've consolidated the three posts into the attached Word document.

We are looking for a light, easy to read design. Good use of graphics to support the message. I've added the graphics we used in the original post.

You can view them at
http://www.quillmarrowgroup.com/blog/are-you-satisfied-with-your-dita-solution/

Target Market(s)

Product managers from High-tech, Finance, and Medical industries.

Industry/Entity Type

Information Technology

Colors

Designer to choose colors to be used in the design.

Requirements
Must have
• Must be modern, light, easy to read and slick design. Try to incorporate the graphics provided, but feel free to add more. Must retain the lists and tables.
• Must align with our website/brand.
• Must be easy to read. So not too busy.
• Please move all footnotes to endnotes. You'll need to rework the numbering.
Nice to have
• Awesome coverpage.
Should not have
• Hokey clipart. Not too heavy or hard to read.

```html
<!DOCTYPE html>
<html lang="en">
<head>
<meta charset="utf-8">
<title>Quill Marrow Group – DITA White Paper Pages</title>
<link href="https://fonts.googleapis.com/css2?family=Exo+2:wght@500;600;700&family=Titillium+Web:ital,wght@0,400;0,600;1,400&display=swap" rel="stylesheet">
<style>
  :root{
    --navy:#2a2d7c;
    --blue:#1fa3db;
    --ink:#3a3a3a;
    --stage:#d9d4cf;
    --paper:#ffffff;
    --foot-gray:#e6e7e9;
    --photo-gray-a:#7f8e9c;
    --photo-gray-b:#5d6d7c;
    --photo-green-a:#2f8a63;
    --photo-green-b:#1d6547;
  }
  *{margin:0;padding:0;box-sizing:border-box}
  html,body{width:1200px;height:1200px;overflow:hidden;background:var(--stage)}
  body{position:relative;font-family:"Titillium Web",sans-serif;color:var(--ink)}
  .page{position:absolute;top:243px;width:505px;height:714px;background:var(--paper);overflow:hidden;box-shadow:0 4px 14px rgba(0,0,0,.25)}
  .page--one{left:68px}
  .page--two{left:627px}
  .page-caption{position:absolute;top:985px;width:505px;text-align:center;font-family:"Titillium Web",sans-serif;font-size:22px;color:#3b3531}
  .page-caption--one{left:68px}.page-caption--two{left:627px}

  /* cover header */
  .brand{position:absolute;left:30px;top:12px;display:flex;align-items:center;gap:8px;z-index:2}
  .brand-dot{width:52px;height:52px;border-radius:50%;background:var(--navy)}
  .brand-name{font-family:"Exo 2",sans-serif;font-weight:700;font-size:15px;line-height:15px;color:var(--navy);width:120px}
  .cover-title{position:absolute;right:30px;top:20px;text-align:right;font-family:"Exo 2",sans-serif;font-weight:600;font-size:18px;line-height:21px;margin:0;z-index:2}
  .cover-title .l1{display:block;font-size:18px;color:#444}
  .cover-title .l2{display:block;font-size:16.5px;color:var(--blue);letter-spacing:.06em;font-weight:700}
  .hero{position:absolute;left:0;top:66px;width:100%;height:208px}
  .hero--gray{background:linear-gradient(90deg,var(--photo-gray-a),var(--photo-gray-b))}
  .rule-blue{position:absolute;left:0;width:100%;height:3px;background:var(--blue)}

  /* page 2 header */
  .part-title{position:absolute;top:26px;width:100%;text-align:center;font-family:"Exo 2",sans-serif;font-weight:700;font-size:23px;line-height:28px;color:var(--navy)}
  .part-title span{color:var(--blue)}
  .split-rule{position:absolute;left:0;width:100%;height:3px;display:flex}
  .split-rule i{display:block;height:100%}
  .split-rule .n{background:var(--navy);width:50%}
  .split-rule .b{background:var(--blue);flex:1}
  .hero--green{top:70px;height:240px;background:linear-gradient(180deg,var(--photo-green-a),var(--photo-green-b))}

  /* body */
  .body{position:absolute;left:30px;right:30px;font-size:7.1px;line-height:8.9px}
  .body p{margin-bottom:6px;text-align:justify}
  .byline{font-size:7.6px;margin-bottom:6px}
  .byline b{font-weight:400;color:var(--blue)}
  .byline em{font-style:italic}
  .section-head{display:flex;align-items:center;margin:6px 0 6px;position:relative;height:30px}
  .section-icon{width:30px;height:30px;border-radius:50%;border:2.5px solid var(--navy);background:#fff;position:relative;z-index:2;display:flex;align-items:center;justify-content:center}
  .section-label{margin-left:-4px;background:var(--blue);color:#fff;font-family:"Exo 2",sans-serif;font-weight:600;font-size:9px;padding:2px 12px 2px 10px;border-radius:0 8px 8px 0;letter-spacing:.02em}
  .cats{display:flex;justify-content:space-between;margin:0 6px 6px 0}
  .bullet{display:flex;align-items:center;gap:5px}
  .bullet::before{content:"";width:7px;height:7px;border-radius:50%;border:1.6px solid var(--blue);flex:none}
  .sub{font-family:"Exo 2",sans-serif;font-weight:600;font-size:9.6px;line-height:12px;color:#555;margin:2px 0 1px}
  .list{margin:10px 0 14px}
  .list .bullet{margin-bottom:8px}

  .footnote{position:absolute;left:0;top:642px;width:100%;height:39px;background:var(--foot-gray);padding:5px 30px;font-size:6.6px;line-height:8.8px;font-style:italic;text-align:justify}
  .footnote b{font-weight:400;color:var(--blue)}
  .footer{position:absolute;left:0;top:683px;width:100%;height:16px;background:var(--blue);color:#fff;text-align:center;font-size:8px;letter-spacing:.35em;line-height:16px}
  .page-num{position:absolute;right:20px;top:677px;width:28px;height:28px;border-radius:50%;background:#fff;border:2.5px solid var(--navy);font-size:9px;color:var(--navy);display:flex;align-items:center;justify-content:center}
</style>
</head>
<body>

<section class="page page--one">
  <div class="brand"><span class="brand-dot"></span><span class="brand-name">QUILL MARROW GROUP</span></div>
  <h1 class="cover-title"><span class="l1">Are you satisfied with</span><span class="l2">YOUR DITA SOLUTION?</span></h1>
  <div class="hero hero--gray" role="img" aria-label="Photo of a doubtful bearded man beside a chalkboard star-rating checklist"></div>
  <div class="rule-blue" style="top:274px"></div>

  <div class="body" style="top:286px">
    <p class="byline">By <b>DANA WHITCOMBE</b> – <em>President of Quill Marrow Group</em></p>
    <p>If your answer is “No” then you are not alone according to a 2017 survey of more than 250 technical communication professionals conducted by The Doc Rancher. The DITA Satisfaction Survey <b style="color:var(--blue);font-weight:400">[i]</b> indicates that 62% of respondents using DITA are—to varying degrees—dissatisfied. As many as 10% of that group were very dissatisfied reporting that their DITA implementation is experiencing ‘big’ challenges. It’s not surprising that there’s significant dissatisfaction amongst those who have adopted DITA. After all, moving to DITA is a seismic shift in technical writing; a big change with many opportunities for things to go wrong.</p>
    <p>The good news is that most DITA users don’t see their problems as insurmountable. Many just need a little help getting to where they’d like to be.</p>

    <div class="section-head">
      <span class="section-icon"><svg width="16" height="16" viewBox="0 0 16 16" fill="none" stroke="#2a2d7c" stroke-width="1.2"><rect x="5.5" y="1" width="5" height="3.5"/><rect x="1" y="11" width="5" height="3.5"/><rect x="10" y="11" width="5" height="3.5"/><path d="M8 4.5v3M3.5 7.5h9M3.5 7.5v3.5M12.5 7.5v3.5"/></svg></span>
      <span class="section-label">BREAKDOWN OF THE ISSUES</span>
    </div>
    <p>The Doc Rancher DITA Satisfaction Survey asked respondents to rank the top 10 issues facing DITA users. These issues fit into three major categories including</p>
    <div class="cats"><span class="bullet">Skills development</span><span class="bullet">Technology</span><span class="bullet">Management</span></div>
    <p>The DITA Satisfaction Survey Aggregate Results revealed little spread between the ranking of the issues indicating that respondents likely faced more than one issue of concern.</p>

    <div class="section-head">
      <span class="section-icon"><svg width="14" height="16" viewBox="0 0 14 16" fill="none" stroke="#2a2d7c" stroke-width="1.2"><rect x="2" y="1" width="10" height="14" rx="1"/><path d="M4.5 5h5M4.5 8h5M4.5 11h5"/></svg></span>
      <span class="section-label">IN THIS ARTICLE</span>
    </div>
    <p>In this article, we examine three issues impacting DITA satisfaction to help you find the best place to start making improvements.</p>
    <h3 class="sub">Part 1: Skills Development</h3>
    <p>This problem area is far and away the most pressing obstacle for a successful DITA deployment. Too often authors are left to figure out how to adapt to writing for DITA on their own.</p>
    <h3 class="sub">Part 2: Technology</h3>
    <p>We often hear about the failure of the technology as it relates to performance or complexity. While technology may seem the most likely culprit, it is often not the root cause of the problem.</p>
    <h3 class="sub">Part 3: Management</h3>
    <p>While these issues appear to be of least concern to many survey respondents, they are most likely to form the root cause of all other issues identified in the survey. This points to a general lack of awareness as to the role management should be playing in</p>
  </div>

  <div class="footnote"><b>[i]</b> DITA Satisfaction Survey published by The Doc Rancher on May 31, 2017. Listen to an analysis of the results by Dana Whitcombe, Owen Tallisford, Harriet Voss, and Leon Marbury and download a copy of the results today from BrightHall at: https://www.brighthall.net/webcast/4410/118204</div>
  <div class="footer">www.quillmarrowgroup.com</div>
  <div class="page-num">01</div>
</section>

<section class="page page--two">
  <h1 class="part-title">PART 1: <span>SKILLS DEVELOPMENT</span></h1>
  <div class="split-rule" style="top:66px"><i class="n"></i><i class="b"></i></div>
  <div class="hero hero--green" role="img" aria-label="Photo of a puzzled man looking up at a green chalkboard reading What am I supposed to do"></div>
  <div class="split-rule" style="top:310px"><i class="n"></i><i class="b"></i></div>

  <div class="body" style="top:328px">
    <p class="byline">By <b>DANA WHITCOMBE</b> – <em>President of Quill Marrow Group</em></p>
    <p style="margin-top:12px">This article is part of a series based on the results of a survey of more than 250 technical communication professionals conducted by The Doc Rancher in 2017 entitled The DITA Satisfaction Survey[i]. In the survey, almost two-thirds of respondents voiced concerns with their DITA deployment.</p>
    <p style="margin-top:10px">In our previous article, we introduced the overall results from the survey that pertain to users’ dissatisfaction with their DITA solution. In this article, we examine the top rated issues pertaining to skills development.</p>

    <div class="section-head" style="margin-top:12px">
      <span class="section-icon"><svg width="16" height="16" viewBox="0 0 16 16" fill="none" stroke="#2a2d7c" stroke-width="1.2"><circle cx="4.5" cy="4" r="2"/><circle cx="11.5" cy="4" r="2"/><path d="M1.5 14v-5a3 3 0 0 1 6 0v5M8.5 14v-5a3 3 0 0 1 6 0v5"/></svg></span>
      <span class="section-label">ISSUES RELATED TO SKILLS DEVELOPMENT</span>
    </div>
    <p>The top-ranked reported issues fall under the category of skill development and training. These include</p>
    <div class="list">
      <div class="bullet">How do I reuse content? Ranked 1st by 75% of respondents</div>
      <div class="bullet">How do I make DITA do what I want it to do? Ranked 2nd by 69% of respondents</div>
      <div class="bullet">Where can I get DITA training? Ranked 3rd by 64% of respondents, and</div>
      <div class="bullet">How do I create DITA content? Ranked 8th by 56% of respondents.</div>
    </div>
    <p>This problem area is far and away the most pressing obstacle for a successful DITA deployment. Too often authors are left to figure out how to adapt to writing for DITA on their own. Organizations will normally invest in tools training—and may even opt for a short training course to learn about DITA—but they rarely make the effort to train writers how to author modular, structured topics of content designed for reuse.</p>
    <p style="margin-top:9px">It is easy to overlook this training aspect and assume that writers will naturally adapt to this new way of writing. But, those assumptions can lead to big problems.</p>
    <p style="margin-top:9px">In a poll conducted in a recent webinar[ii] where half of the participants indicated they were already using DITA, a full 70% indicated that they had no formal DITA training. Of those participants, nearly 60% were self-taught while the others had no training at all. It’s no wonder that dissatisfaction is the norm.</p>
  </div>

  <div class="footer">www.quillmarrowgroup.com</div>
  <div class="page-num">02</div>
</section>

<div class="page-caption page-caption--one">PAGE-1</div>
<div class="page-caption page-caption--two">PAGE-2</div>

</body>
</html>
```